fun, modern poster design for office environment

We are a Corporate Health consultants and are looking for posters encouraging staff to be healthy.
Wanted: A5 poster design encouraging office workers to take the stairs rather than lift.
Posters will be displayed around the office and near the stairs
Poster will have health benefits included and should have a fun modern feel.
More poster designs to follow.

Target Market(s)

Men and some aged between 20 and 55.

Industry/Entity Type

Environment

Font styles to use
Sans Serif

Colors
0792cd
00a990
9ccb3b
86cfc6
fbf289
fcca95
ffffff
3277b5

Requirements
Must have
• A5 size
• Wording 'take the stairs' and a health benefit of taking be stairs.
• My company logo and name Brightwell Collective
• Web address www.brightwellcollective.com.au
Nice to have
• Images and words
Should not have
• Stick people or people images.

```html
<!DOCTYPE html>
<html lang="en">
<head>
<meta charset="utf-8">
<title>Take the Stairs – Brightwell Collective</title>
<link href="https://fonts.googleapis.com/css2?family=Nunito:wght@400;600&display=swap" rel="stylesheet">
<style>
  :root {
    --page: #ffffff;
    --sky: #b4e3f1;
    --stair: #f6b978;
    --navy: #1d3a64;
    --teal: #3aaea0;
    --title-blue: #3277b5;
    --sub-blue: #1a8fd0;
    --mark-green: #9ccb3b;
  }
  html, body {
    margin: 0;
    padding: 0;
    overflow: hidden;
    background: var(--page);
  }
  .poster {
    position: relative;
    width: 1200px;
    height: 1000px;
    background: var(--page);
    font-family: "Nunito", sans-serif;
    overflow: hidden;
  }
  .poster-art {
    position: absolute;
    left: 0;
    top: 0;
  }
  .brand {
    position: absolute;
    left: 60px;
    top: 136px;
    width: 410px;
    text-align: center;
  }
  .brand-mark {
    width: 192px;
    height: 192px;
    margin: 0 auto;
    border-radius: 50%;
    background: var(--mark-green);
  }
  .brand-name {
    margin: 20px 0 0;
    font-size: 34px;
    font-weight: 400;
    color: var(--navy);
    line-height: 1.2;
  }
  .brand-web {
    margin: 16px 0 0;
    font-size: 20px;
    font-weight: 400;
    color: var(--navy);
  }
  .brand-phone {
    margin: 18px 0 0;
    font-size: 19px;
    font-weight: 400;
    color: var(--teal);
  }
  .headline {
    position: absolute;
    left: 560px;
    top: 490px;
    width: 580px;
    margin: 0;
    text-align: center;
    font-size: 60px;
    font-weight: 400;
    color: var(--title-blue);
    line-height: 1.2;
  }
  .tagline {
    position: absolute;
    left: 560px;
    top: 642px;
    width: 580px;
    margin: 0;
    text-align: center;
    font-size: 42px;
    font-weight: 400;
    color: var(--sub-blue);
    line-height: 1.35;
  }
</style>
</head>
<body>
<main class="poster">
  <svg class="poster-art" width="1200" height="1000" viewBox="0 0 1200 1000">
    <defs>
      <clipPath id="panel-clip">
        <rect x="41" y="86" width="1122" height="825"/>
      </clipPath>
    </defs>
    <rect class="sky-panel" x="41" y="86" width="1122" height="825" fill="var(--sky)" aria-hidden="true"/>
    <polygon class="stair-band" role="img" aria-label="Staircase illustration rising from lower left to upper right"
      clip-path="url(#panel-clip)" fill="var(--stair)"
      points="41,800 1010,86 1097,86 1097,92 90,846 41,846"/>
  </svg>

  <header class="brand">
    <div class="brand-mark"></div>
    <p class="brand-name">Brightwell Collective</p>
    <p class="brand-web">www.brightwellcollective.com.au</p>
    <p class="brand-phone">1300 555 018</p>
  </header>

  <h1 class="headline">Take the Stairs</h1>
  <p class="tagline">Step up to a<br>healthier lifestyle</p>
</main>
</body>
</html>
```